Hydrographic business needs a business card that reaches hunters and off-road enthusiasts

We need a business card for a new hydrographics company catering to customers such as hunters, off-road ATV riders and custom vehicle enthusiasts. A western theme is preferred but professional. Our service should be thought of as upper end graphic design on firearms, off road vehicles, motorcycles, etc... See www.caldorfx.com for ideas on patterns, colors, etc...

Target Market(s)

Hunters, off road enthusiasts, custom car enthusiasts, motorcycle riders...

Industry/Entity Type

Graphic Design

```html
<!DOCTYPE html>
<html lang="en">
<head>
<meta charset="utf-8">
<title>Caldor Dip Works – Business Card</title>
<link rel="stylesheet" href="https://fonts.googleapis.com/css2?family=Bree+Serif&family=Open+Sans:wght@300;400;700;800&family=Oswald:wght@500;600&display=swap">
<style>
  :root {
    --canvas-bg: #e9e6e2;
    --cream: #f7e4cd;
    --cream-stripe: rgba(190, 150, 110, 0.10);
    --charcoal: #2f2e2f;
    --charcoal-stripe: rgba(255, 255, 255, 0.035);
    --copper: #d49670;
    --copper-dark: #c07c54;
    --ink: #333132;
    --ink-soft: #4a4748;
    --white: #f4f1ec;
  }
  * { box-sizing: border-box; margin: 0; padding: 0; }
  html, body { width: 1200px; height: 1200px; overflow: hidden; }
  body {
    background: var(--canvas-bg);
    display: flex;
    flex-direction: column;
    align-items: center;
    justify-content: center;
    gap: 56px;
    font-family: "Open Sans", Arial, sans-serif;
  }
  .card {
    width: 880px;
    height: 503px;
    position: relative;
    overflow: hidden;
    box-shadow: 0 6px 18px rgba(0,0,0,0.18);
  }
  .card--front {
    background:
      repeating-linear-gradient(-60deg, var(--cream-stripe) 0 2px, transparent 2px 6px),
      var(--cream);
    color: var(--ink);
  }
  .card--back {
    background:
      repeating-linear-gradient(-60deg, var(--charcoal-stripe) 0 2px, transparent 2px 6px),
      var(--charcoal);
    color: var(--white);
    display: flex;
    align-items: center;
    justify-content: center;
  }

  /* Contact column */
  .contact {
    position: absolute;
    left: 64px;
    top: 58px;
    width: 400px;
  }
  .contact__name {
    font-family: "Bree Serif", Georgia, serif;
    font-size: 46px;
    line-height: 1;
    color: var(--copper-dark);
    letter-spacing: 1px;
    text-transform: uppercase;
  }
  .contact__role {
    margin-top: 8px;
    font-weight: 800;
    font-size: 15px;
    letter-spacing: 0.5px;
    text-transform: uppercase;
    color: var(--ink);
  }
  .contact__address {
    margin-top: 26px;
    font-weight: 400;
    font-size: 27px;
    line-height: 1.2;
    text-transform: uppercase;
    color: var(--ink-soft);
  }
  .contact__rule {
    height: 2px;
    width: 340px;
    background: var(--ink);
    margin: 22px 0;
  }
  .contact__phone {
    font-weight: 800;
    font-size: 44px;
    letter-spacing: 1px;
    line-height: 1;
  }
  .contact__web {
    font-weight: 300;
    font-size: 21px;
    line-height: 1.35;
    text-transform: uppercase;
    color: var(--ink-soft);
    letter-spacing: 0.5px;
  }

  /* Brand lockup */
  .brand {
    display: flex;
    flex-direction: column;
    align-items: center;
    text-align: center;
  }
  .card--front .brand {
    position: absolute;
    right: 50px;
    top: 50%;
    transform: translateY(-50%);
    width: 340px;
  }
  .brand__disc {
    width: 210px;
    height: 210px;
    border-radius: 50%;
    background: var(--copper);
  }
  .brand__name {
    margin-top: 22px;
    font-family: "Oswald", "Arial Narrow", sans-serif;
    font-weight: 600;
    font-size: 32px;
    letter-spacing: 1px;
    text-transform: uppercase;
    line-height: 1.1;
  }
  .card--front .brand__name { color: var(--ink); }
  .brand__tagline {
    margin-top: 10px;
    font-family: "Oswald", "Arial Narrow", sans-serif;
    font-weight: 500;
    font-size: 14px;
    letter-spacing: 0.6px;
    text-transform: uppercase;
  }
  .card--front .brand__tagline { color: var(--ink-soft); }
  .card--back .brand__disc { width: 240px; height: 240px; }
  .card--back .brand__name { color: var(--white); font-size: 36px; }
  .card--back .brand__tagline { color: var(--white); font-size: 15px; }
</style>
</head>
<body>

  <section class="card card--front" aria-label="Business card front">
    <div class="contact">
      <h1 class="contact__name">Wade Caldor</h1>
      <p class="contact__role">Web &amp; Graphic Designer</p>
      <p class="contact__address">512 Mesa Ridge Road<br>Cedar Flats, TX 75001</p>
      <div class="contact__rule"></div>
      <p class="contact__phone">214 555 0187</p>
      <div class="contact__rule"></div>
      <p class="contact__web">wade@caldorfx.com<br>www.caldorfx.com</p>
    </div>

    <div class="brand">
      <div class="brand__disc"></div>
      <p class="brand__name">Caldor Dip Works</p>
      <p class="brand__tagline">Custom water transfer finishes built tough for the Lone Star trail</p>
    </div>
  </section>

  <section class="card card--back" aria-label="Business card back">
    <div class="brand">
      <div class="brand__disc"></div>
      <p class="brand__name">Caldor Dip Works</p>
      <p class="brand__tagline">Custom water transfer finishes built tough for the Lone Star trail</p>
    </div>
  </section>

</body>
</html>
```